New Company Newsletter Template Needed!!!

We need some new graphics/design for us to create our company newsletter in MS Publisher/Word. Prefer simple, modern design that can be easy to update each month, flexible for adding images and include our company logo (attached).
Also attached our basic existing template but we do not want to use the same “swoosh” ribbon and want to reduce the number of colours used.
Needs to be elements we can move into the software and create a PDF newsletter to circulate.

Font styles to use
Sans Serif

Requirements
Must have
• Company logo
Nice to have
• If any colours should fit into our company logo palette

```html
<!DOCTYPE html>
<html lang="en">
<head>
<meta charset="utf-8">
<title>Company Newsletter</title>
<link rel="stylesheet" href="https://fonts.googleapis.com/css2?family=Barlow:wght@300;400;700&display=swap">
<style>
  :root {
    --page: #ebebed;
    --panel: #cfd0d2;
    --placeholder: #9b9c9e;
    --rule: #a9aaad;
    --orange: #f3a600;
    --blue: #0a3e94;
    --red-orange: #e64016;
    --text: #2b2b2b;
    --date: #1d3f94;
    --white: #ffffff;
  }
  * { margin: 0; padding: 0; box-sizing: border-box; }
  html, body { width: 842px; height: 1200px; overflow: hidden; background: var(--page); }
  .page {
    position: relative;
    width: 842px;
    height: 1200px;
    overflow: hidden;
    background: var(--page);
    font-family: "Barlow", Arial, sans-serif;
  }
  .page-graphics { position: absolute; inset: 0; }
  .image-slot {
    position: absolute;
    left: 295px;
    width: 492px;
    background: var(--placeholder);
    display: flex;
    align-items: center;
    justify-content: center;
    color: var(--white);
    font-weight: 700;
    font-size: 56px;
    letter-spacing: 1px;
  }
  .image-slot--top { top: 56px; height: 430px; }
  .image-slot--bottom { top: 505px; height: 396px; }
  .section-rule {
    position: absolute;
    left: 292px;
    top: 494px;
    width: 550px;
    height: 1px;
    background: var(--rule);
  }
  .masthead-title {
    position: absolute;
    left: 208px;
    top: 663px;
    transform-origin: 0 0;
    transform: rotate(-90deg);
    font-weight: 700;
    font-size: 88px;
    line-height: 1;
    letter-spacing: 1px;
    color: rgba(255,255,255,0.55);
    white-space: nowrap;
  }
  .intro-copy {
    position: absolute;
    left: 295px;
    top: 918px;
    width: 373px;
    font-weight: 300;
    font-size: 15px;
    line-height: 31px;
    color: var(--text);
    text-align: justify;
  }
  .issue-date {
    position: absolute;
    left: 615px;
    top: 1068px;
    font-size: 15px;
    font-weight: 400;
    color: var(--date);
  }
</style>
</head>
<body>
<div class="page">
  <svg class="page-graphics" width="842" height="1200" viewBox="0 0 842 1200">
    <defs>
      <linearGradient id="mastheadPhotoTone" x1="0" y1="0" x2="0" y2="1">
        <stop offset="0" stop-color="#4fb99a"/>
        <stop offset="0.45" stop-color="#2cb0c9"/>
        <stop offset="1" stop-color="#63c6dc"/>
      </linearGradient>
      <clipPath id="panelClip"><rect x="0" y="45" width="799" height="1112"/></clipPath>
    </defs>
    <rect class="content-panel" x="0" y="45" width="799" height="1112" fill="var(--panel)"/>
    <g class="decor-circles" clip-path="url(#panelClip)" fill="none" stroke="#a9aaad" stroke-width="1">
      <circle cx="520" cy="1040" r="325"/>
      <circle cx="-190" cy="785" r="200"/>
      <circle cx="528" cy="1195" r="125"/>
    </g>
    <circle class="decor-disc" cx="789" cy="1114" r="71" fill="#e2e3e5" clip-path="url(#panelClip)"/>
    <line x1="695" y1="1200" x2="760" y2="1094" stroke="#a9aaad" stroke-width="1"/>
    <polygon class="accent-stripe" points="42,0 65,0 65,637 42,613" fill="var(--orange)"/>
    <polygon class="masthead-photo" role="img" aria-label="Masthead photo strip in teal and turquoise tones"
             points="65,0 208,0 208,771 65,637" fill="url(#mastheadPhotoTone)"/>
    <polygon class="side-band" points="73,670 240,829 240,1200 73,1200" fill="var(--blue)"/>
    <polygon class="date-tab" points="615,1094 756,1094 697,1157 615,1157" fill="var(--red-orange)"/>
    <line x1="756" y1="1094" x2="697" y2="1157" stroke="#ffffff" stroke-width="3" opacity="0.7"/>
  </svg>

  <div class="masthead-title">NEWSLETTER</div>

  <div class="image-slot image-slot--top">PICTURE 1</div>
  <div class="section-rule"></div>
  <div class="image-slot image-slot--bottom">PICTURE 2</div>

  <p class="intro-copy">Also attached our basic existing template but we do not want to use the same “swoosh” ribbon and want to reduce the number of colours used.</p>

  <div class="issue-date">Monday 25 May 2020</div>
</div>
</body>
</html>
```